Carver Lindqvist Group Business Cards

We have a new logo, and want to design new business cards with it. We are 21 years in business, and want a fresh but professional look, so not a lot of extra stuff on the card. We are a recruiting and staffing firm focused on placing accounting and finance professionals in the Dallas TX area. I've attached our new logo that should be displayed on the cards. Here is what I think we want on the cards:
Ray Pemberly, CPA
Partner and Managing Director
8282 Orchard Vale Rd.
Suite 610
Dallas, TX 75391
O 214-555-0184
M 214-555-0237
ray@carverlindqvist.example
www.carverlindqvist.example

```html
<!DOCTYPE html>
<html lang="en">
<head>
<meta charset="utf-8">
<title>Carver Lindqvist Group – Business Card</title>
<link href="https://fonts.googleapis.com/css2?family=Montserrat:wght@600;700&family=Open+Sans:wght@400&display=swap" rel="stylesheet">
<style>
  :root {
    --page-bg: #e9e6e1;
    --card-bg: #232323;
    --frame-blue: #2c46b0;
    --brand-blue: #3554c4;
    --ink-light: #f4f4f4;
    --ink-muted: #e2e2e2;
  }
  * { box-sizing: border-box; margin: 0; padding: 0; }
  html, body {
    width: 1200px; height: 900px; overflow: hidden;
    background: var(--page-bg);
  }
  .card {
    position: absolute; left: 75px; top: 150px;
    width: 1050px; height: 600px;
    background: var(--card-bg);
    box-shadow: 0 10px 30px rgba(0,0,0,.25);
  }
  .card__frame {
    position: absolute; inset: 28px;
    border: 3px solid var(--frame-blue);
  }
  .brand {
    position: absolute; left: 150px; top: 92px;
    display: flex; align-items: center; gap: 14px;
  }
  .brand__mark {
    width: 22px; height: 22px; background: var(--brand-blue);
  }
  .brand__name {
    font-family: "Montserrat", sans-serif; font-weight: 700;
    font-size: 30px; color: var(--brand-blue); letter-spacing: .5px;
  }
  .person {
    position: absolute; left: 112px; top: 268px;
    color: var(--ink-light);
  }
  .person__name {
    font-family: "Montserrat", sans-serif; font-weight: 700;
    font-size: 30px; letter-spacing: .5px;
  }
  .person__title {
    margin-top: 14px;
    font-family: "Open Sans", sans-serif; font-size: 20px;
    letter-spacing: 2.5px; color: var(--ink-muted);
  }
  .contact {
    position: absolute; right: 92px; top: 280px;
    font-family: "Open Sans", sans-serif; font-size: 20px;
    letter-spacing: 1.6px; color: var(--ink-light);
    list-style: none;
  }
  .contact__row {
    display: flex; align-items: center; justify-content: flex-end; gap: 34px;
  }
  .contact__text { text-align: right; line-height: 30px; }
  .contact__icon { width: 20px; height: 20px; flex: none; }
  .contact__row--address { margin-bottom: 14px; }
  .contact__row--address .contact__text { line-height: 31px; }
</style>
</head>
<body>
  <div class="card">
    <div class="card__frame"></div>

    <div class="brand">
      <span class="brand__mark"></span>
      <span class="brand__name">Carver Lindqvist Group</span>
    </div>

    <div class="person">
      <div class="person__name">Ray Pemberly, CPA</div>
      <div class="person__title">Partner and Managing Director</div>
    </div>

    <ul class="contact">
      <li class="contact__row contact__row--address">
        <span class="contact__text">8282 Orchard Vale Rd.<br>Suite 610<br>Dallas, TX 75391</span>
        <svg class="contact__icon" viewBox="0 0 20 20" aria-hidden="true"><path d="M10 1a6 6 0 0 0-6 6c0 4.5 6 11 6 11s6-6.5 6-11a6 6 0 0 0-6-6z" fill="#fff"/><circle cx="10" cy="7" r="2.3" fill="#232323"/></svg>
      </li>
      <li class="contact__row">
        <span class="contact__text">214-555-0184</span>
        <svg class="contact__icon" viewBox="0 0 20 20" aria-hidden="true"><path d="M5 2l3 4-2 2c1 2.5 3.5 5 6 6l2-2 4 3-2 3C9 18 2 11 2 5z" fill="#fff"/></svg>
      </li>
      <li class="contact__row">
        <span class="contact__text">214-555-0237</span>
        <svg class="contact__icon" viewBox="0 0 20 20" aria-hidden="true"><rect x="5" y="1" width="10" height="18" rx="2" fill="#fff"/><rect x="7" y="4" width="6" height="10" fill="#232323"/></svg>
      </li>
      <li class="contact__row">
        <span class="contact__text">ray@carverlindqvist.example</span>
        <svg class="contact__icon" viewBox="0 0 20 20" aria-hidden="true"><rect x="1" y="4" width="18" height="12" fill="#fff"/><path d="M1 4l9 7 9-7" fill="none" stroke="#232323" stroke-width="1.5"/></svg>
      </li>
      <li class="contact__row">
        <span class="contact__text">www.carverlindqvist.example</span>
        <svg class="contact__icon" viewBox="0 0 20 20" aria-hidden="true"><circle cx="10" cy="10" r="8.5" fill="#fff"/><path d="M1.5 10h17M10 1.5c-3 3-3 14 0 17M10 1.5c3 3 3 14 0 17M3 6h14M3 14h14" fill="none" stroke="#232323" stroke-width="1"/></svg>
      </li>
    </ul>
  </div>
</body>
</html>
```